Mirela Hastow ADHD coach needs a flyer

I need a flyer to be sent by email. the copy is attached. It can be changed/reduced to fit the flyer. I would like to keep my website colors. My website is www.mirelahastow.example - Thank you!

```html
<!DOCTYPE html>
<html lang="en">
<head>
<meta charset="utf-8">
<title>Mirela Hastow – ADHD and Academic Coach</title>
<link rel="stylesheet" href="https://fonts.googleapis.com/css2?family=Cinzel:wght@400;700&family=Open+Sans:wght@300;400;600&family=Exo+2:ital,wght@0,700;1,700&family=EB+Garamond:ital@1&display=swap">
<style>
:root{
  --band:#6b7471;
  --band-mid:#8f9a9a;
  --band-light:#c9cfd1;
  --footer:#3a3f3e;
  --panel:#363b3a;
  --headline-box:#8a9596;
  --name-box:#d6e1e7;
  --page-left:#e9eaeb;
  --page-right:#b4bcc1;
  --ink:#3a3f40;
  --ink-soft:#4a4f50;
  --panel-text:#d9dddd;
  --accent:#1d8fd4;
  --tick:#7dc2df;
  --quote-bg:#e5e8ee;
  --white:#ffffff;
}
*{margin:0;padding:0;box-sizing:border-box}
html,body{width:1200px;height:2240px;overflow:hidden;background:#fff}
.flyer{position:relative;width:1200px;height:2240px;overflow:hidden;
  background:linear-gradient(90deg,var(--page-left) 0%,#dfe2e4 45%,var(--page-right) 100%);
  font-family:"Open Sans",Arial,sans-serif;color:var(--ink)}
.abs{position:absolute}
.top-band{left:0;top:0;width:1200px;height:80px;background:var(--band);
  display:flex;align-items:center;justify-content:center;gap:28px;color:#fff;
  font-family:"Cinzel",serif;font-size:36px;letter-spacing:1px;padding-left:5px}
.top-band .sep{font-family:"Open Sans",sans-serif;font-weight:300}
.portrait{left:500px;top:80px;width:700px;height:1052px;
  background:radial-gradient(ellipse at 55% 60%,#f3e0e0 0%,#e8d6d8 28%,#b9b5bd 52%,#a9b3b9 75%)}
.name-light{left:8px;top:100px;width:345px;height:118px;background:var(--name-box)}
.name-dark{left:353px;top:100px;width:395px;height:118px;background:rgba(210,216,220,.55)}
.name{top:92px;left:92px;font-size:116px;font-weight:400;letter-spacing:-2px;line-height:1;white-space:nowrap}
.name .first{color:#3c4240;text-shadow:4px 4px 0 #aab4b8}
.name .last{color:#fff;margin-left:30px;text-shadow:-2px 0 0 #56605f,3px 3px 0 #56605f}
.headline-box{left:18px;top:245px;width:745px;height:205px;background:var(--headline-box);padding:8px 12px 0 12px}
.headline{font-family:"Cinzel",serif;color:#fff;font-size:32px;line-height:40px;font-weight:400}
.subhead{font-size:20.5px;line-height:25px;color:#2f3433;margin-top:-2px}
.intro{left:43px;top:462px;width:590px;font-size:18.6px;line-height:27.4px;color:var(--ink-soft);letter-spacing:.2px}
.intro p+p{margin-top:27px}
.dropcap{float:left;font-size:92px;line-height:74px;margin:6px 6px 0 -2px;color:#3a3f40;font-weight:300}
.panel-right{left:1100px;top:1180px;width:100px;height:530px;background:var(--panel)}
.panel{left:0;top:1132px;width:690px;height:640px;background:var(--panel);
  clip-path:polygon(0 0,620px 0,690px 20px,690px 640px,0 640px)}
.panel-inner{left:42px;top:1148px;width:600px;color:var(--panel-text)}
.panel-title{font-family:"Exo 2",sans-serif;font-weight:700;font-size:29px;color:var(--accent)}
.panel-title em{color:#fff}
.panel-lead{font-size:18.5px;line-height:30px;margin:12px 0 14px 6px}
.ticks{list-style:none}
.ticks li{position:relative;padding-left:54px;font-size:18.5px;line-height:32px}
.ticks svg{position:absolute;left:8px;top:4px;width:26px;height:26px}
.card{left:672px;top:1087px;width:453px;height:698px;background:#fff;padding:45px 20px 0 24px}
.card h2{font-family:"Exo 2",sans-serif;font-weight:700;color:var(--accent);font-size:30px;line-height:34px}
.card h3{font-family:"Exo 2",sans-serif;font-weight:700;font-style:italic;color:#3a3f40;font-size:25px;line-height:26px;margin-bottom:16px}
.card .ticks li{padding-left:40px;line-height:34.5px;color:#3a3f40;font-size:18.5px}
.card .ticks svg{left:-2px;top:5px}
.card h2.second{margin:6px 0 6px}
.quotes{left:8px;top:1790px;width:1184px;height:255px;background:var(--quote-bg)}
.quote-col{top:1815px;text-align:center;font-family:"EB Garamond",serif;font-style:italic;font-size:17.5px;line-height:22px;color:#333}
.quote-col h4{font-family:"Open Sans",sans-serif;font-style:normal;font-weight:600;font-size:24px;color:#5a6060;margin-bottom:26px}
.quote-col p+p{margin-top:22px}
.quote-col .who{font-style:normal}
.cta{left:0;top:2065px;width:1200px;height:135px}
.cta-text{left:67px;top:2080px;color:#fff}
.cta-text strong{display:block;font-family:"Exo 2",sans-serif;font-size:44px;line-height:46px;color:var(--accent)}
.cta-text span{display:block;font-size:26px;line-height:24px;letter-spacing:.5px}
.cta-phone{left:483px;top:2150px;font-size:26px;color:#fff;letter-spacing:.5px}
.cta-mail{left:790px;top:2150px;font-size:26px;color:#4e5656;letter-spacing:.5px}
.footer{left:0;top:2195px;width:1200px;height:45px;background:var(--footer);color:#fff;
  text-align:center;font-size:26px;font-weight:600;line-height:45px}
</style>
</head>
<body>
<div class="flyer">
  <header class="abs top-band"><span>Ph.D.</span><span class="sep">|</span><span>ADHD and Academic Coach</span></header>

  <div class="abs portrait" role="img" aria-label="Portrait photograph of the coach in a pale pink blazer with arms crossed"></div>

  <div class="abs name-light"></div>
  <div class="abs name-dark"></div>
  <h1 class="abs name"><span class="first">MIRELA</span><span class="last">HASTOW</span></h1>

  <section class="abs headline-box">
    <h2 class="headline">Helping Your Child with ADHD or Other Learning Challenges Thrive in College and Beyond</h2>
    <p class="subhead">Academic success coaching that leads to lifelong transformation for students with ADHD and similar challenges that may have impeded their ability to thrive.</p>
  </section>

  <div class="abs intro">
    <p><span class="dropcap">S</span>ending your child off to college can feel scary, especially if that college is hundreds of miles away. You worry about how they'll do on their own—whether they'll make friends, earn good grades, and be happy—especially without you there to support them daily. You know your child is bright, and you want them to have a great future, but you're concerned they will struggle without the right support and resources.</p>
    <p>You don't need to feel helpless as you send your child off to this next stage of their lives. Mirela is dedicated to making that transition easier for everyone. Mirela Hastow has years of experience helping students thrive despite their challenges. She sees your child's potential and helps them see it, too. She provides a safety net as they adjust to a new environment at college.<br>Her services are comprehensive and adaptable, based on the requirements of each individual: helping with course selection and scheduling, time management, study strategies, focus, making new friends, and adapting to change. Through it all, Mirela guides students through fundamental work on mindset to ensure that changes stick.</p>
  </div>

  <div class="abs panel-right"></div>
  <div class="abs panel"></div>
  <section class="abs panel-inner">
    <h2 class="panel-title">Empowering Focus: <em>How Mirela Helps</em></h2>
    <p class="panel-lead">Mirela has taken students from failing to a 3.0 GPA, and from a C student to the Dean's List, in just one semester. It doesn't take years to provide lasting results; all it takes is the right guide.</p>
    <ul class="ticks">
      <li><svg viewBox="0 0 26 26"><circle cx="13" cy="13" r="11" fill="#fff" stroke="var(--tick)" stroke-width="3"/><path d="M8 13.5l3.5 3.5 7-8" fill="none" stroke="#3a5a66" stroke-width="2.4"/></svg>Uniquely positioned to help your child, Mirela:</li>
      <li><svg viewBox="0 0 26 26"><circle cx="13" cy="13" r="11" fill="#fff" stroke="var(--tick)" stroke-width="3"/><path d="M8 13.5l3.5 3.5 7-8" fill="none" stroke="#3a5a66" stroke-width="2.4"/></svg>Tailors support so that your child improves focus and maximizes their potential in college and beyond.</li>
      <li><svg viewBox="0 0 26 26"><circle cx="13" cy="13" r="11" fill="#fff" stroke="var(--tick)" stroke-width="3"/><path d="M8 13.5l3.5 3.5 7-8" fill="none" stroke="#3a5a66" stroke-width="2.4"/></svg>Understands your child's unique needs - she sees the gifts that others often miss.</li>
      <li><svg viewBox="0 0 26 26"><circle cx="13" cy="13" r="11" fill="#fff" stroke="var(--tick)" stroke-width="3"/><path d="M8 13.5l3.5 3.5 7-8" fill="none" stroke="#3a5a66" stroke-width="2.4"/></svg>Knows the academic landscape intimately, including the challenges faced by students with ADHD and other conditions.</li>
      <li><svg viewBox="0 0 26 26"><circle cx="13" cy="13" r="11" fill="#fff" stroke="var(--tick)" stroke-width="3"/><path d="M8 13.5l3.5 3.5 7-8" fill="none" stroke="#3a5a66" stroke-width="2.4"/></svg>Helps with the logistics of scheduling in a way that most advisors can't, enrolling students in the courses that best suit their learning style.</li>
      <li><svg viewBox="0 0 26 26"><circle cx="13" cy="13" r="11" fill="#fff" stroke="var(--tick)" stroke-width="3"/><path d="M8 13.5l3.5 3.5 7-8" fill="none" stroke="#3a5a66" stroke-width="2.4"/></svg>Nurtures the brilliance in your bright child.</li>
      <li><svg viewBox="0 0 26 26"><circle cx="13" cy="13" r="11" fill="#fff" stroke="var(--tick)" stroke-width="3"/><path d="M8 13.5l3.5 3.5 7-8" fill="none" stroke="#3a5a66" stroke-width="2.4"/></svg>Provides a balance between encouraging students and challenging them.</li>
    </ul>
  </section>

  <section class="abs card">
    <h2>Realizing Potential:</h2>
    <h3>The Transformation<br>You'll See in Your Child</h3>
    <ul class="ticks">
      <li><svg viewBox="0 0 26 26"><circle cx="13" cy="13" r="11" fill="#9aa2a3" stroke="#5d6566" stroke-width="2"/><path d="M8 13.5l3.5 3.5 7-8" fill="none" stroke="#fff" stroke-width="2.4"/></svg>A mindset of self-belief and increased confidence.</li>
      <li><svg viewBox="0 0 26 26"><circle cx="13" cy="13" r="11" fill="#9aa2a3" stroke="#5d6566" stroke-width="2"/><path d="M8 13.5l3.5 3.5 7-8" fill="none" stroke="#fff" stroke-width="2.4"/></svg>Higher grades and the drive to graduate.</li>
      <li><svg viewBox="0 0 26 26"><circle cx="13" cy="13" r="11" fill="#9aa2a3" stroke="#5d6566" stroke-width="2"/><path d="M8 13.5l3.5 3.5 7-8" fill="none" stroke="#fff" stroke-width="2.4"/></svg>Social integration and making friends.</li>
      <li><svg viewBox="0 0 26 26"><circle cx="13" cy="13" r="11" fill="#9aa2a3" stroke="#5d6566" stroke-width="2"/><path d="M8 13.5l3.5 3.5 7-8" fill="none" stroke="#fff" stroke-width="2.4"/></svg>Happiness and fulfilment.</li>
      <li><svg viewBox="0 0 26 26"><circle cx="13" cy="13" r="11" fill="#9aa2a3" stroke="#5d6566" stroke-width="2"/><path d="M8 13.5l3.5 3.5 7-8" fill="none" stroke="#fff" stroke-width="2.4"/></svg>A deep sense of personal achievement and pride.</li>
    </ul>
    <h2 class="second">You Will Have:</h2>
    <ul class="ticks">
      <li><svg viewBox="0 0 26 26"><circle cx="13" cy="13" r="11" fill="#9aa2a3" stroke="#5d6566" stroke-width="2"/><path d="M8 13.5l3.5 3.5 7-8" fill="none" stroke="#fff" stroke-width="2.4"/></svg>Less stress, knowing that your child is in good hands.</li>
      <li><svg viewBox="0 0 26 26"><circle cx="13" cy="13" r="11" fill="#9aa2a3" stroke="#5d6566" stroke-width="2"/><path d="M8 13.5l3.5 3.5 7-8" fill="none" stroke="#fff" stroke-width="2.4"/></svg>Fewer sleepless nights worrying about your child.</li>
      <li><svg viewBox="0 0 26 26"><circle cx="13" cy="13" r="11" fill="#9aa2a3" stroke="#5d6566" stroke-width="2"/><path d="M8 13.5l3.5 3.5 7-8" fill="none" stroke="#fff" stroke-width="2.4"/></svg>Confidence that they are receiving the right support.</li>
      <li><svg viewBox="0 0 26 26"><circle cx="13" cy="13" r="11" fill="#9aa2a3" stroke="#5d6566" stroke-width="2"/><path d="M8 13.5l3.5 3.5 7-8" fill="none" stroke="#fff" stroke-width="2.4"/></svg>Joy and pride at seeing them do well.</li>
    </ul>
  </section>

  <div class="abs quotes"></div>
  <section class="abs quote-col" style="left:30px;width:545px">
    <h4>What Parents Say</h4>
    <p>“Mirela was the glue that kept our daughter in college… as our daughter's Academic Coach, [she] gave our daughter the ability to finish strong by empowering her with the skills needed to be successful.”<span class="who">—Renata</span></p>
    <p>“Mirela has always told my daughter not that she can succeed, but that she will succeed.”<span class="who">—Lorna</span></p>
  </section>
  <section class="abs quote-col" style="left:625px;width:545px">
    <h4>What Students Say</h4>
    <p>"Last semester I completed all 16 hours and I had the highest GPA I've ever had!" <span class="who">—Former student</span></p>
    <p>“Under her instruction, my grades began to improve. I ended up making the Dean's List during my time at Halbrook, and I was also inducted into Tau Delta Rho. I am currently in my first year of law school at Westmere University, a top tier school.”<span class="who">—Former student</span></p>
  </section>

  <svg class="abs cta" viewBox="0 0 1200 135" aria-hidden="true">
    <rect width="1200" height="135" fill="var(--band-light)"/>
    <polygon points="0,0 820,0 760,135 0,135" fill="var(--band-mid)"/>
    <polygon points="0,0 515,0 455,135 0,135" fill="var(--band)"/>
    <g fill="none" stroke="#fff" stroke-width="2">
      <rect x="606" y="22" width="24" height="44" rx="4"/>
      <line x1="606" y1="30" x2="630" y2="30"/>
      <line x1="606" y1="58" x2="630" y2="58"/>
      <rect x="946" y="33" width="42" height="28" rx="2"/>
      <polyline points="946,33 967,50 988,33"/>
    </g>
  </svg>
  <div class="abs cta-text"><strong>Next Steps</strong><span>To learn more and discuss</span><span>your child's individual needs,</span></div>
  <div class="abs cta-phone">call 555·201·4318 or,</div>
  <div class="abs cta-mail">email coach@mirelahastow.example</div>

  <footer class="abs footer">www.mirelahastow.example</footer>
</div>
</body>
</html>
```